Wren's Home Care Retractable Banner Design

Retractable Banner Design
We need a pull up retractable banner design
85 x 206 cm.
We need the banner to use at expo's, information sessions, presentations, recruitment days. Needs to be attractive to our elderly client's and staff (care workers)
Phone number needs to be on 08 6937 4426
Website also needs to be on the banner : wrenshomecare.com.au

Target Market(s)

35 +

Industry/Entity Type

aged care / community

Requirements
Must have
• Colours, fonts and logo as detailed in upload

```html
<!DOCTYPE html>
<html lang="en">
<head>
<meta charset="UTF-8">
<title>Wren's Home Care – Pull Up Banner</title>
<link rel="stylesheet" href="https://fonts.googleapis.com/css2?family=Poppins:wght@400;700&display=swap">
<style>
  :root {
    --brand-red: #931a2b;
    --ink: #1c1c1c;
    --paper: #ffffff;
    --backdrop: #e9e9e9;
    --photo-warm: #9b8874;
    --photo-light: #d8c9b6;
    --photo-dark: #5c4c40;
  }
  * { margin: 0; padding: 0; box-sizing: border-box; }
  html, body {
    width: 1200px; height: 1200px; overflow: hidden;
    background: var(--backdrop);
    font-family: "Poppins", sans-serif;
  }
  .banner {
    position: absolute; left: 365px; top: 50px;
    width: 470px; height: 1100px;
    background: var(--paper);
    overflow: hidden;
  }
  .banner-shapes { position: absolute; inset: 0; width: 100%; height: 100%; }

  .brand { position: absolute; left: 42px; top: 98px; display: flex; align-items: center; }
  .brand-dot {
    width: 44px; height: 44px; border-radius: 50%;
    background: var(--brand-red); flex: none;
  }
  .brand-name {
    margin-left: 16px; color: var(--brand-red);
    font-weight: 400; font-size: 32px; line-height: 40px; white-space: nowrap;
  }

  .headline { position: absolute; left: 42px; top: 282px; color: var(--ink); }
  .headline-lead { font-size: 48px; font-weight: 400; line-height: 62px; }
  .headline-accent { font-size: 46px; font-weight: 700; line-height: 60px; color: var(--brand-red); }

  .benefits { position: absolute; left: 44px; top: 522px; list-style: none; }
  .benefits li {
    display: flex; align-items: center;
    font-size: 18px; line-height: 38px; color: var(--ink);
  }
  .benefits li::before {
    content: ""; width: 12px; height: 12px; border-radius: 50%;
    background: var(--brand-red); margin-right: 18px; flex: none;
  }

  .contact { position: absolute; left: 42px; top: 980px; list-style: none; color: var(--paper); }
  .contact li { display: flex; align-items: center; font-size: 21px; line-height: 40px; }
  .contact svg { width: 18px; height: 18px; margin-right: 16px; flex: none; }
</style>
</head>
<body>
  <main class="banner">
    <svg class="banner-shapes" viewBox="0 0 300 692" preserveAspectRatio="none" aria-hidden="true">
      <defs>
        <linearGradient id="photo-tone" x1="0" y1="0" x2="1" y2="1">
          <stop offset="0" stop-color="var(--photo-dark)"/>
          <stop offset="0.5" stop-color="var(--photo-light)"/>
          <stop offset="1" stop-color="var(--photo-warm)"/>
        </linearGradient>
      </defs>
      <path class="care-photo" role="img" aria-label="Photo of a smiling young carer hugging an elderly man at home"
            d="M0,590 C70,545 130,480 175,420 C205,378 215,330 240,313 C262,302 282,300 300,300 L300,560 L0,620 Z"
            fill="url(#photo-tone)"/>
      <path class="divider-line" d="M0,606 C100,594 220,556 300,532" fill="none" stroke="#ffffff" stroke-width="3"/>
      <path class="contact-band" d="M0,614 C100,602 220,564 300,540 L300,692 L0,692 Z" fill="var(--brand-red)"/>
    </svg>

    <header class="brand">
      <div class="brand-dot" aria-hidden="true"></div>
      <p class="brand-name">Wren's Home Care</p>
    </header>

    <h1 class="headline">
      <span class="headline-lead">After all its</span><br>
      <span class="headline-accent">Your Home,<br>Your Care</span>
    </h1>

    <ul class="benefits">
      <li>Family-owned and local.</li>
      <li>Hassle-free,quality care.</li>
      <li>Peace of mind for families.</li>
      <li>Nurse-led expertise.</li>
    </ul>

    <ul class="contact">
      <li>
        <svg viewBox="0 0 24 24" fill="#ffffff"><path d="M6.6 10.8a15.1 15.1 0 0 0 6.6 6.6l2.2-2.2a1 1 0 0 1 1-.25 11.4 11.4 0 0 0 3.6.57 1 1 0 0 1 1 1V20a1 1 0 0 1-1 1A17 17 0 0 1 3 4a1 1 0 0 1 1-1h3.5a1 1 0 0 1 1 1c0 1.25.2 2.45.57 3.57a1 1 0 0 1-.25 1z"/></svg>
        08 6937 4426
      </li>
      <li>
        <svg viewBox="0 0 24 24" fill="none" stroke="#ffffff" stroke-width="2"><circle cx="12" cy="12" r="9"/><path d="M3 12h18M12 3c3 3.2 3 14.8 0 18M12 3c-3 3.2-3 14.8 0 18"/></svg>
        wrenshomecare.com.au
      </li>
    </ul>
  </main>
</body>
</html>
```